"Tova's" Website Design

Tova's makes earth friendly, healthy, and delicious snacks that are completely gluten free. We are looking for a website that is easy to navigate, energetic, and conveys our purpose "To create healthy, earth-friendly, gluten free snacks that fill bellies and warm hearts."
Our first product is "Tova's Cheese Bursts" are a small, square, cracker pack with an unreasonable amount of cheddar cheese flavor. The flavor literally explodes in your mouth!
We really want our site to pop and show off some personality.
I'm attaching the logo for the company, feel free to go beyond the logo in terms of color.
Here are some sites that we like!
http://www.pollwinkle.example/company
http://www.brenmoor.example/
http://www.qx47.example/
http://www.teddyvales.example/
http://www.dunrise.example/food/products_zest/
http://www.marvelfrost.example/

```html
<!DOCTYPE html>
<html lang="en">
<head>
<meta charset="utf-8">
<title>Tova's — Gluten free snacks</title>
<link href="https://fonts.googleapis.com/css2?family=Mystery+Quest&family=PT+Sans&family=Arimo&display=swap" rel="stylesheet">
<style>
  :root {
    --page-bg: #eff0f2;
    --brand-orange: #ee6129;
    --footer-orange: #ef602b;
    --cheese-light: #fbc94d;
    --cheese-deep: #f2ac2c;
    --berry: #9b1c5f;
    --leaf: #6bbf5b;
    --forest: #11663a;
    --nav-grey: #6e6e70;
    --body-grey: #6b6b6b;
    --social-yellow: #f7c530;
    --white: #ffffff;
  }
  * { margin: 0; padding: 0; box-sizing: border-box; }
  html, body { width: 1200px; height: 938px; overflow: hidden; }
  body { background: var(--page-bg); font-family: "Arimo", Arial, sans-serif; position: relative; }

  .site-header { position: absolute; top: 0; left: 0; width: 1200px; height: 131px; }
  .brand { position: absolute; left: 124px; top: 18px; font-family: "Mystery Quest", cursive; font-size: 76px; line-height: 1; color: var(--brand-orange); }
  .main-nav { position: absolute; top: 20px; right: 123px; display: flex; gap: 29px; }
  .main-nav a { font-family: "PT Sans", sans-serif; font-size: 22px; color: var(--nav-grey); text-decoration: none; text-transform: uppercase; letter-spacing: 0.2px; }

  .hero { position: absolute; top: 131px; left: 0; width: 1200px; height: 363px;
    background: radial-gradient(ellipse at 60% 40%, var(--cheese-light), var(--cheese-deep)); overflow: hidden; }
  .hero-product { position: absolute; left: 64px; top: 24px; width: 364px; height: 294px; border-radius: 30px;
    background: linear-gradient(160deg, #e9b777, #c98446); }
  .hero-copy { position: absolute; left: 503px; top: 84px; }
  .hero-new { font-family: "Mystery Quest", cursive; font-size: 86px; line-height: 0.9; color: var(--berry); text-shadow: 3px 3px 0 var(--white); }
  .hero-title { font-family: "Mystery Quest", cursive; font-size: 64px; line-height: 1; color: var(--berry); text-shadow: 3px 3px 0 var(--white); white-space: nowrap; }
  .hero-title .name { color: var(--leaf); }
  .hero-tagline { margin-top: 14px; font-size: 28px; color: var(--forest); }
  .slider-dots { position: absolute; top: 325px; left: 570px; display: flex; gap: 11px; }
  .slider-dots span { width: 21px; height: 21px; border-radius: 50%; background: var(--white); box-shadow: 1px 1px 3px rgba(0,0,0,.3); }
  .slider-dots .active { background: var(--cheese-deep); border: 4px solid var(--white); }

  .features { position: absolute; top: 532px; left: 135px; display: flex; gap: 80px; }
  .feature { width: 257px; }
  .feature h2 { font-family: "Mystery Quest", cursive; font-weight: 400; font-size: 31px; margin-bottom: 15px; }
  .feature:nth-child(1) h2 { color: var(--forest); }
  .feature:nth-child(2) h2 { color: var(--berry); }
  .feature:nth-child(3) h2 { color: var(--brand-orange); }
  .feature p { font-size: 10.6px; line-height: 13.6px; color: var(--body-grey); }

  .site-footer { position: absolute; top: 740px; left: 0; width: 1200px; height: 198px; }
  .footer-wave { position: absolute; top: 0; left: 0; }
  .footer-body { position: absolute; top: 12px; left: 0; width: 1200px; height: 186px; background: var(--footer-orange); }
  .footer-col { position: absolute; top: 35px; color: var(--white); }
  .footer-col h3 { font-weight: 400; font-size: 17px; margin-bottom: 9px; }
  .footer-col p, .footer-col a { display: block; font-size: 11px; line-height: 13.6px; color: var(--white); text-decoration: none; }
  .col-address { left: 140px; }
  .col-links { left: 330px; }
  .col-social { left: 516px; }
  .social-list { display: flex; gap: 18px; margin-top: 6px; }
  .social-item { display: flex; align-items: center; gap: 7px; font-size: 12px; color: var(--white); text-decoration: none; }
  .social-item span { width: 40px; height: 40px; border-radius: 50%; background: var(--social-yellow); box-shadow: 2px 2px 3px rgba(0,0,0,.25); }
</style>
</head>
<body>
  <header class="site-header">
    <div class="brand">Tova's</div>
    <nav class="main-nav">
      <a href="#">About us</a>
      <a href="#">Products</a>
      <a href="#">Where to buy</a>
      <a href="#">Contacts</a>
    </nav>
  </header>

  <section class="hero">
    <div class="hero-product" role="img" aria-label="Stack of square cheese crackers with two lightning bolts"></div>
    <div class="hero-copy">
      <div class="hero-new">New</div>
      <div class="hero-title"><span class="name">Tova's</span>Cheesebursts</div>
      <p class="hero-tagline">The flavor literally explodes in your mouth!</p>
    </div>
    <div class="slider-dots"><span class="active"></span><span></span><span></span></div>
  </section>

  <section class="features">
    <article class="feature">
      <h2>Gluten free snacks</h2>
      <p>Gluten-free snacks seem challenging, but really the list below looks very similar to what you might have eaten as a snack before you went gluten-free. Even though you might think these snack ideas are fairly obvious, generating even the most obvious ideas helps me keep a good supply of healthy and frugal snacks in the house.</p>
    </article>
    <article class="feature">
      <h2>Gluten free snacks</h2>
      <p>Gluten-free snacks seem challenging, but really the list below looks very similar to what you might have eaten as a snack before you went gluten-free. Even though you might think these snack ideas are fairly obvious, generating even the most obvious ideas helps me keep a good supply of healthy and frugal snacks in the house.</p>
    </article>
    <article class="feature">
      <h2>Gluten free snacks</h2>
      <p>Gluten-free snacks seem challenging, but really the list below looks very similar to what you might have eaten as a snack before you went gluten-free. Even though you might think these snack ideas are fairly obvious, generating even the most obvious ideas helps me keep a good supply of healthy and frugal snacks in the house.</p>
    </article>
  </section>

  <footer class="site-footer">
    <svg class="footer-wave" width="1200" height="14" viewBox="0 0 1200 14" aria-hidden="true">
      <path d="M0 14 L0 8 Q6 0 12 8 Q18 0 24 8 Q30 0 36 8 Q42 0 48 8 Q54 0 60 8 Q66 0 72 8 Q78 0 84 8 Q90 0 96 8 Q102 0 108 8 Q114 0 120 8 Q126 0 132 8 Q138 0 144 8 Q150 0 156 8 Q162 0 168 8 Q174 0 180 8 Q186 0 192 8 Q198 0 204 8 Q210 0 216 8 Q222 0 228 8 Q234 0 240 8 Q246 0 252 8 Q258 0 264 8 Q270 0 276 8 Q282 0 288 8 Q294 0 300 8 Q306 0 312 8 Q318 0 324 8 Q330 0 336 8 Q342 0 348 8 Q354 0 360 8 Q366 0 372 8 Q378 0 384 8 Q390 0 396 8 Q402 0 408 8 Q414 0 420 8 Q426 0 432 8 Q438 0 444 8 Q450 0 456 8 Q462 0 468 8 Q474 0 480 8 Q486 0 492 8 Q498 0 504 8 Q510 0 516 8 Q522 0 528 8 Q534 0 540 8 Q546 0 552 8 Q558 0 564 8 Q570 0 576 8 Q582 0 588 8 Q594 0 600 8 Q606 0 612 8 Q618 0 624 8 Q630 0 636 8 Q642 0 648 8 Q654 0 660 8 Q666 0 672 8 Q678 0 684 8 Q690 0 696 8 Q702 0 708 8 Q714 0 720 8 Q726 0 732 8 Q738 0 744 8 Q750 0 756 8 Q762 0 768 8 Q774 0 780 8 Q786 0 792 8 Q798 0 804 8 Q810 0 816 8 Q822 0 828 8 Q834 0 840 8 Q846 0 852 8 Q858 0 864 8 Q870 0 876 8 Q882 0 888 8 Q894 0 900 8 Q906 0 912 8 Q918 0 924 8 Q930 0 936 8 Q942 0 948 8 Q954 0 960 8 Q966 0 972 8 Q978 0 984 8 Q990 0 996 8 Q1002 0 1008 8 Q1014 0 1020 8 Q1026 0 1032 8 Q1038 0 1044 8 Q1050 0 1056 8 Q1062 0 1068 8 Q1074 0 1080 8 Q1086 0 1092 8 Q1098 0 1104 8 Q1110 0 1116 8 Q1122 0 1128 8 Q1134 0 1140 8 Q1146 0 1152 8 Q1158 0 1164 8 Q1170 0 1176 8 Q1182 0 1188 8 Q1194 0 1200 8 L1200 14 Z" fill="#ef602b"/>
    </svg>
    <div class="footer-body">
      <div class="footer-col col-address">
        <h3>Tova's</h3>
        <p>18 Fennel Row</p>
        <p>Marbury</p>
        <p>MB4 7QX</p>
        <p>Westshire</p>
        <p>ENGLAND</p>
        <p>United Kingdom</p>
      </div>
      <div class="footer-col col-links">
        <h3>Quicklinks</h3>
        <a href="#">About us</a>
        <a href="#">Products</a>
        <a href="#">Where to buy</a>
        <a href="#">Contacts</a>
      </div>
      <div class="footer-col col-social">
        <h3>Follow us</h3>
        <div class="social-list">
          <a class="social-item" href="#"><span></span>Chirply</a>
          <a class="social-item" href="#"><span></span>Friendnook</a>
        </div>
      </div>
    </div>
  </footer>
</body>
</html>
```